ALL ASPECTS OF PLASTERING INC: TEXTURE,SANDFINISH RENO,POOLS, PATCH WORK ( STATEWIDE SERVICE GOOD RATES) 100% GUARANTEED FULLY INSURED C

Target Market(s)

ANYONE WHO OWNS A HOUSE,BUILDERS

Industry/Entity Type

Work

Contact Information for Business Card

GRITT-WALL PLASTERING SERVICES
BERNARD KOVALEC 0438259164
EMAIL:TARVEK48@QUILLMAIL.COM

Requirements
Must have
• COLOUR BACKGROUND WIV PLASTERING PICTURE EG TROWEL, CEMENT MIXER, SAND
Nice to have
• BOLD PROFESSIONAL LOOKING AND SOUNDING CATCHY SAYING
Should not have
• FLURO COLOURS

```html
<!DOCTYPE html>
<html lang="en">
<head>
<meta charset="utf-8">
<title>Gritt-Wall Plastering Services – Business Card</title>
<link href="https://fonts.googleapis.com/css2?family=Audiowide&family=Open+Sans:wght@700&family=Questrial&display=swap" rel="stylesheet">
<style>
  :root {
    --board: #ebeced;
    --plaster-light: #f6f6f4;
    --plaster-mid: #e4e4e1;
    --plaster-shade: #d3d3cf;
    --orange: #ef7d18;
    --charcoal: #2b2b2b;
    --navy: #1f2d4e;
    --ink: #4a4a4a;
    --white: #ffffff;
  }
  html, body {
    margin: 0;
    padding: 0;
    width: 993px;
    height: 1200px;
    overflow: hidden;
    background: var(--board);
  }
  .board {
    position: relative;
    width: 993px;
    height: 1200px;
  }
  .card {
    position: absolute;
    width: 758px;
    height: 475px;
    border-radius: 25px;
    overflow: hidden;
    box-shadow: 0 6px 16px rgba(0,0,0,0.22);
  }
  .card--front { left: 109px; top: 76px; }
  .card--back  { left: 102px; top: 625px; }

  .plaster-photo {
    position: absolute;
    inset: 0;
    background:
      linear-gradient(100deg, var(--plaster-shade) 0%, var(--plaster-mid) 22%, var(--plaster-light) 55%, var(--plaster-mid) 100%);
  }
  .card--back .plaster-photo {
    background:
      linear-gradient(80deg, var(--plaster-light) 0%, var(--plaster-light) 50%, var(--plaster-mid) 75%, var(--plaster-shade) 100%);
  }

  .contact-band {
    position: absolute;
    left: 0; right: 0;
    top: 354px; bottom: 0;
    background: var(--charcoal);
    border-top: 5px solid var(--orange);
  }

  .brand, .name, .contact { position: absolute; right: 96px; margin: 0; text-align: right; white-space: nowrap; }
  .brand-name {
    top: 104px;
    font-family: "Audiowide", sans-serif;
    font-size: 44px;
    line-height: 1;
    color: var(--orange);
    letter-spacing: 1px;
  }
  .brand-tagline {
    top: 172px;
    font-family: "Audiowide", sans-serif;
    font-size: 26px;
    line-height: 1;
    color: var(--charcoal);
    letter-spacing: 1px;
  }
  .name {
    top: 306px;
    font-family: "Open Sans", sans-serif;
    font-weight: 700;
    font-size: 24px;
    line-height: 1;
    color: var(--navy);
  }
  .contact {
    font-family: "Open Sans", sans-serif;
    font-weight: 700;
    font-size: 26px;
    line-height: 1;
    color: var(--white);
    display: flex;
    align-items: center;
    gap: 12px;
  }
  .contact--phone { top: 380px; }
  .contact--email { top: 423px; }
  .contact svg { fill: none; stroke: var(--white); stroke-width: 2; }

  .services {
    position: absolute;
    left: 56px;
    top: 94px;
    margin: 0;
  }
  .services-heading {
    margin: 0 0 8px;
    font-family: "Open Sans", sans-serif;
    font-weight: 700;
    font-size: 22px;
    line-height: 30px;
    color: var(--orange);
  }
  .services-list {
    list-style: none;
    margin: 0;
    padding: 0;
    font-family: "Questrial", sans-serif;
    font-size: 23px;
    line-height: 30px;
    color: var(--ink);
  }
  .services-list li {
    position: relative;
    padding-left: 36px;
  }
  .services-list li::before {
    content: "";
    position: absolute;
    left: 7px;
    top: 11px;
    width: 8px;
    height: 8px;
    background: var(--orange);
    transform: rotate(45deg);
  }
  .services-list .note { display: block; }
</style>
</head>
<body>
<main class="board">

  <section class="card card--front">
    <div class="plaster-photo" role="img" aria-label="Photo of a hand spreading wet plaster on a wall with a steel trowel"></div>
    <h1 class="brand brand-name">GRITT-WALL</h1>
    <p class="brand brand-tagline">PLASTERING SERVICES</p>
    <p class="name">BERNARD KOVALEC</p>
    <div class="contact-band"></div>
    <p class="contact contact--phone">
      <svg width="22" height="22" viewBox="0 0 24 24" aria-hidden="true"><path d="M5 3h4l2 5-2.5 1.5a11 11 0 0 0 6 6L16 13l5 2v4a2 2 0 0 1-2 2A17 17 0 0 1 3 5a2 2 0 0 1 2-2z"/></svg>
      0438259164
    </p>
    <p class="contact contact--email">
      <svg width="26" height="20" viewBox="0 0 26 20" aria-hidden="true"><rect x="1.5" y="2" width="23" height="16"/><path d="M1.5 2l11.5 9 11.5-9M1.5 18l8.5-8M24.5 18l-8.5-8"/></svg>
      tarvek48@quillmail.com
    </p>
  </section>

  <section class="card card--back">
    <div class="plaster-photo" role="img" aria-label="Faded photo of a hand holding a plastering trowel against a smooth wall"></div>
    <div class="services">
      <h2 class="services-heading">All aspects of plastering:</h2>
      <ul class="services-list">
        <li>Texture</li>
        <li>Sandfinish reno</li>
        <li>Pools</li>
        <li>Patch work <span class="note">(statewide service good rates)</span></li>
        <li>100% guaranteed fully insured</li>
      </ul>
    </div>
  </section>

</main>
</body>
</html>
```